Marketing Agency Portfolio Brochure

Copper Reed Meridian Holdings is a marketing entity representing diverse brands and services. We are seeking a graphic designer to create a corporate brochure template that showcases the unique offerings of four distinct categories: Equestrian Facility, Freestyle Motocross Team, Aerobatic Team, and Property Portfolio. The brochure should have a sophisticated corporate look and feel, allowing for easy expansion and customization in the future.

Brand Details:

Company Name: Copper Reed Meridian Holdings
Tone: Corporate, Professional, Versatile
Brochure Structure:

Each category will have a four-page spread.
Page 1: Introduction to the specific product or brand.
Pages 2-4: Presentation of offerings, details, and key highlights.
Category Details:

Equestrian Facility:

Introduction: Brief overview of the equestrian facility.
Offering Pages: Showcase services, amenities, and unique features.
Freestyle Motocross Team:

Introduction: Brief overview of the freestyle motocross team.
Offering Pages: Highlight team achievements, members, and upcoming events.
Aerobatic Team:

Introduction: Brief overview of the aerobatic team.
Offering Pages: Showcase team expertise, performances, and services offered.
Property Portfolio:

Introduction: Brief overview of the property portfolio.
Offering Pages: Showcase properties, locations, and key features.
Design Requirements:

Corporate Look and Feel:

Professional and versatile design suitable for a corporate audience.
Consistent color scheme and typography throughout.
Template Flexibility:

Allow for easy customization and expansion for future additions or modifications.
Maintain a cohesive design for each category while allowing for unique elements.
Visual Elements:

Use high-quality images representative of each category.
Incorporate clean and modern layouts.
Updates

Sample needs to make provision for all categories, not only one. the brochure needs to have a cover page with the main logo

```html
<!DOCTYPE html>
<html lang="en">
<head>
<meta charset="utf-8">
<title>Copper Reed Meridian Holdings – Portfolio Brochure</title>
<link href="https://fonts.googleapis.com/css2?family=Poppins:wght@200;300;400;500;600;700&display=swap" rel="stylesheet">
<style>
:root{
  --stage:#353535;
  --paper:#ffffff;
  --ink:#111111;
  --ink-soft:#3a3a3a;
  --rule:#6b6b6b;
  --bar:#d3d3d6;
  --photo-dark:#2a2a2a;
  --photo-mid:#7a7a7a;
  --photo-light:#cfcfcf;
}
*{margin:0;padding:0;box-sizing:border-box}
html,body{width:1200px;height:1200px;overflow:hidden;background:var(--stage)}
body{font-family:'Poppins',sans-serif;color:var(--ink)}
.spread{position:relative;width:1200px;height:1200px}
.page{position:absolute;width:346px;height:488px;background:var(--paper);overflow:hidden}
.page > *{position:absolute}
.p-cover{left:70px;top:80px}
.p-welcome{left:426px;top:80px}
.p-services{left:784px;top:80px}
.p-features{left:70px;top:582px}
.p-amenities{left:426px;top:582px}
.p-team{left:784px;top:582px}

/* header */
.hline{height:1px;background:var(--rule)}
.page-no{width:19px;height:19px;border:1px solid var(--ink);border-radius:50%;font-size:6.5px;display:flex;align-items:center;justify-content:center;background:var(--paper)}
.brand-mini{font-size:5.2px;font-weight:500;letter-spacing:.4px;line-height:1.25;text-transform:uppercase;width:62px;color:var(--ink)}
.brand-mini.light{color:#fff}

.lorem{font-size:6.6px;line-height:1.3;color:var(--ink-soft);text-align:justify}
.lorem.left{text-align:left}

/* cover */
.cover-deco{left:0;top:0;width:346px;height:488px}
.cover-brand{left:52px;top:62px;width:240px;font-size:21px;font-weight:400;letter-spacing:1.6px;line-height:1.25;text-transform:uppercase;color:var(--ink)}
.cover-bar{left:43px;top:333px;width:2px;height:108px;background:var(--ink)}
.cover-title{left:50px;top:330px;font-size:29px;font-weight:200;line-height:37px;letter-spacing:.4px;color:var(--ink)}

/* welcome */
.welcome-hero{left:0;top:70px;width:346px;height:182px}
.welcome-tab{left:0;top:106px;width:25px;height:18px;background:#e9e9e9}
.welcome-head{left:51px;top:111px;color:#fff}
.welcome-head h1{font-size:17px;font-weight:300;letter-spacing:.5px}
.welcome-head h2{font-size:10px;font-weight:300;margin-top:1px}
.welcome-head p{font-size:6.8px;line-height:1.72;font-weight:300;width:130px;margin-top:8px}
.intro-box{left:38px;top:277px;width:142px;height:164px;border:1.2px solid var(--ink);padding:14px 12px 0 12px}
.intro-box .ib-head{display:flex;gap:7px;align-items:center;margin-bottom:10px}
.intro-box .ib-kicker{font-size:6px;font-weight:500}
.intro-box .ib-title{font-size:10px;font-weight:500;line-height:1.05}
.intro-box .lorem{margin-bottom:8px}
.welcome-side{left:196px;top:293px;width:110px}
.welcome-side .divider{height:1px;background:var(--ink);margin:13px 0 15px}

/* services */
.services-hero{left:0;top:70px;width:346px;height:182px}
.services-title{right:52px;top:97px;text-align:right}
.services-title span{display:block;font-size:10px;font-weight:300}
.services-title strong{display:block;font-size:17px;font-weight:600;line-height:1.05}
.services-intro{left:99px;top:183px;width:195px}
.svc{left:99px;width:202px}
.svc-bar{position:relative;height:15px;background:var(--bar);font-size:7.8px;display:flex;align-items:center;padding-left:33px}
.svc-num{position:absolute;left:-3px;top:-1.5px;width:18px;height:18px;border-radius:50%;background:var(--ink);color:#fff;font-size:8px;font-weight:600;display:flex;align-items:center;justify-content:center}
.svc-row{display:flex;font-size:6.8px;height:14px;align-items:center;border-bottom:1px solid #bdbdbd;margin-left:3px}
.svc-row b{font-weight:400;width:32px}

/* features */
.features-photo{left:0;top:0;width:346px;height:244px}
.features-head{left:180px;top:70px}
.features-head span{display:block;font-size:10.5px;font-weight:300}
.features-head strong{display:block;font-size:16.5px;font-weight:400;line-height:1.05}
.features-copy{left:182px;top:111px;width:132px}
.features-copy h4{font-size:6.8px;font-weight:600;margin:13px 0 13px}
.features-aside{left:28px;top:264px;width:100px;border-top:1px solid var(--ink);padding-top:11px}
.features-aside h4{font-size:7px;font-weight:600;line-height:1.25;padding-left:3px;margin-bottom:19px}
.features-aside .lorem{margin-bottom:7px}
.feature{width:66px}
.feature .f-head{display:flex;gap:5px;align-items:center;margin-bottom:5px}
.feature .f-icon{width:21px;height:21px;border:1px solid var(--ink);display:flex;align-items:center;justify-content:center;flex:none}
.feature .f-name{font-size:6.6px;font-weight:500;line-height:1.2}
.feature .lorem{text-align:left;font-size:6.8px}

/* amenities */
.amen-bar{left:37px;top:77px;width:2px;height:26px;background:var(--ink)}
.amen-head{left:46px;top:74px}
.amen-head span{display:block;font-size:12px;font-weight:300;line-height:1.1}
.amen-head strong{display:block;font-size:16.5px;font-weight:700;line-height:1.1}
.amenity{width:78px;text-align:center}
.amenity .a-icon{width:48px;height:48px;border-radius:50%;background:var(--ink);margin:0 auto 7px;display:flex;align-items:center;justify-content:center}
.amenity h5{font-size:7px;font-weight:500}
.amenity .a-sub{font-size:5.8px;margin:2px 0 5px}
.amenity .lorem{font-size:5.6px;line-height:1.24}
.amen-photo{left:38px;top:337px;width:120px;height:103px}
.testi{left:177px;top:338px;width:128px}
.testi h6{font-size:6.4px;font-weight:400;margin-bottom:4px}
.testi .quote{font-size:9px;line-height:.6}
.testi .lorem{font-size:6.2px;padding-bottom:4px;border-bottom:1px solid #bdbdbd;margin-bottom:8px}
.testi ul{list-style:none}
.testi li{font-size:6.4px;margin-bottom:5px;padding-left:9px;position:relative}
.testi li::before{content:"";position:absolute;left:0;top:3px;width:3px;height:3px;border-radius:50%;background:var(--ink)}

/* team */
.team-photo{left:0;top:0;width:346px;height:234px}
.team-head{left:55px;top:77px;color:#fff}
.team-head span{display:block;font-size:11px;font-weight:400}
.team-head strong{display:block;font-size:17px;font-weight:600;line-height:1.05}
.team-shapes{left:0;top:0;width:346px;height:488px}
.team-brand{left:196px;top:196px;width:94px;font-size:6.5px;font-weight:500;letter-spacing:.6px;line-height:1.3;text-transform:uppercase;color:#fff;text-align:center}
.member{width:92px}
.member h5{font-size:7.6px;font-weight:600;margin-bottom:1px}
.member p{font-size:6.4px;line-height:1.25;color:var(--ink-soft)}
.member.right{text-align:right}
</style>
</head>
<body>
<main class="spread">

  <!-- cover -->
  <section class="page p-cover">
    <svg class="cover-deco" viewBox="0 0 346 488" aria-hidden="true">
      <defs>
        <linearGradient id="coverFade" x1="0" y1="0" x2="1" y2="1">
          <stop offset="0" stop-color="#f4f4f4"/><stop offset="1" stop-color="#ffffff"/>
        </linearGradient>
      </defs>
      <polygon points="0,0 120,0 240,150 346,40 346,200 250,300 60,60 0,60" fill="url(#coverFade)"/>
      <polygon points="20,300 110,190 346,420 346,488 20,488" fill="#f5f5f5"/>
      <polygon points="180,230 346,120 346,260" fill="#f7f7f7"/>
      <polygon points="110,190 180,230 20,360 20,300" fill="#efefef"/>
    </svg>
    <div class="cover-brand">Copper Reed Meridian Holdings</div>
    <div class="cover-bar"></div>
    <h1 class="cover-title">REPRESENTING<br>DIVERSE BRANDS<br>AND SERVICES</h1>
  </section>

  <!-- welcome -->
  <section class="page p-welcome">
    <div class="hline" style="left:0;top:30px;width:54px"></div>
    <div class="page-no" style="left:62px;top:21px">1</div>
    <div class="hline" style="left:89px;top:30px;width:139px"></div>
    <div class="brand-mini" style="left:244px;top:20px">Copper Reed Meridian Holdings</div>
    <div class="hline" style="left:306px;top:30px;width:40px"></div>
    <svg class="welcome-hero" viewBox="0 0 346 182">
      <defs>
        <linearGradient id="officeTone" x1="0" y1="0" x2="1" y2="1">
          <stop offset="0" stop-color="#3a3a3a"/><stop offset="1" stop-color="#1e1e1e"/>
        </linearGradient>
        <linearGradient id="cityTone" x1="0" y1="0" x2="0" y2="1">
          <stop offset="0" stop-color="#d8d8d8"/><stop offset=".5" stop-color="#8a8a8a"/><stop offset="1" stop-color="#4a4a4a"/>
        </linearGradient>
      </defs>
      <rect width="346" height="182" fill="url(#officeTone)" role="img" aria-label="Photo of a business meeting in a dim office"/>
      <polygon points="158,0 174,0 346,182 330,182" fill="#ffffff"/>
      <polygon points="174,0 346,0 346,182" fill="url(#cityTone)" role="img" aria-label="Photo of a city skyline with skyscrapers"/>
      <rect x="0" y="182" width="346" height="0" fill="#fff"/>
    </svg>
    <div class="welcome-tab"></div>
    <div class="welcome-head">
      <h1>WELCOME</h1>
      <h2>OF&nbsp; EQUESTRIAN FACILITY</h2>
      <p>Lorem Ipsum is simply dummy text of the printing and typesetting industry. Lorem Ipsum has been the industry's standard dummy text ever since the 1500s, When an unknown printer took</p>
    </div>
    <div class="intro-box">
      <div class="ib-head">
        <svg width="22" height="22" viewBox="0 0 22 22" aria-hidden="true">
          <rect x="1" y="1" width="20" height="20" fill="#111"/>
          <path d="M4 6h10M4 9h8M4 12h6M4 15h5" stroke="#fff" stroke-width="1.2"/>
          <path d="M10 18l8-8 2 2-8 8h-2z" fill="#fff"/>
        </svg>
        <div><div class="ib-kicker">EQUESTRIAN FACILITY</div><div class="ib-title">INTRODUCTION</div></div>
      </div>
      <p class="lorem">Lorem Ipsum is simply dummy text of the printing and typesetting industry. Lorem Ipsum has been the industry's standard dummy text ever since the 1500s, when an unknown printer took a galley of type and scrambled it to make a type specimen book.</p>
      <p class="lorem left">Lorem Ipsum is simply dummy text of the printing and typesetting industry.</p>
    </div>
    <div class="welcome-side">
      <p class="lorem left">Lorem Ipsum is simply dummy text of the printing and typesetting industry. Lorem Ipsum has been.</p>
      <div class="divider"></div>
      <p class="lorem">Lorem Ipsum is simply dummy text of the printing and typesetting industry. Lorem Ipsum has been the industry's standard dummy text ever since he 1500s, when an unknown printer took a galley of type and crambled it to make a type specimen book.</p>
    </div>
  </section>

  <!-- services -->
  <section class="page p-services">
    <div class="hline" style="left:0;top:30px;width:52px"></div>
    <div class="brand-mini" style="left:57px;top:20px">Copper Reed Meridian Holdings</div>
    <div class="hline" style="left:122px;top:30px;width:141px"></div>
    <div class="page-no" style="left:262px;top:24px">2</div>
    <div class="hline" style="left:306px;top:30px;width:40px"></div>
    <svg class="services-hero" viewBox="0 0 346 182">
      <polygon points="0,0 170,0 0,182" fill="url(#cityTone2)" role="img" aria-label="Photo of a city skyline with skyscrapers"/>
      <defs>
        <linearGradient id="cityTone2" x1="0" y1="0" x2="0" y2="1">
          <stop offset="0" stop-color="#d8d8d8"/><stop offset=".5" stop-color="#8a8a8a"/><stop offset="1" stop-color="#4a4a4a"/>
        </linearGradient>
      </defs>
    </svg>
    <svg style="left:80px;top:92px" width="8" height="8" aria-hidden="true"><circle cx="4" cy="4" r="3.6" fill="#111"/></svg>
    <div class="services-title"><span>LIST OF</span><strong>SERVICES</strong></div>
    <p class="lorem services-intro">Lorem Ipsum is simply dummy text of the printing and typesetting industry. Lorem Ipsum has been the industry's standard dummy text ever since the 1500s, when an unknown printer took.</p>
    <div class="svc" style="top:241px">
      <div class="svc-bar"><span class="svc-num">1</span>Our Services 1</div>
      <div class="svc-row"><b>00</b>Lorem Ipsum is simply dummy</div>
      <div class="svc-row"><b>00</b>Lorem Ipsum is simply dummy</div>
    </div>
    <div class="svc" style="top:301px">
      <div class="svc-bar"><span class="svc-num">2</span>Our Services 2</div>
      <div class="svc-row"><b>00</b>Lorem Ipsum is simply dummy</div>
      <div class="svc-row"><b>00</b>Lorem Ipsum is simply dummy</div>
      <div class="svc-row"><b>00</b>Lorem Ipsum is simply dummy</div>
    </div>
    <div class="svc" style="top:377px">
      <div class="svc-bar"><span class="svc-num">3</span>Our Services 3</div>
      <div class="svc-row"><b>00</b>Lorem Ipsum is simply dummy</div>
      <div class="svc-row"><b>00</b>Lorem Ipsum is simply dummy</div>
      <div class="svc-row"><b>00</b>Lorem Ipsum is simply dummy</div>
    </div>
  </section>

  <!-- features -->
  <section class="page p-features">
    <svg class="features-photo" viewBox="0 0 346 244">
      <defs>
        <linearGradient id="laptopTone" x1="0" y1="0" x2="1" y2="1">
          <stop offset="0" stop-color="#e6e6e6"/><stop offset=".55" stop-color="#9a9a9a"/><stop offset="1" stop-color="#3c3c3c"/>
        </linearGradient>
      </defs>
      <path d="M0 0H346V42H151V244H0Z" fill="url(#laptopTone)" role="img" aria-label="Photo of a laptop with floating business chart icons"/>
    </svg>
    <div class="hline" style="left:0;top:30px;width:54px"></div>
    <div class="page-no" style="left:67px;top:24px">5</div>
    <div class="hline" style="left:95px;top:30px;width:216px"></div>
    <div class="brand-mini" style="left:252px;top:19px">Copper Reed Meridian Holdings</div>
    <div class="features-head"><span>OUR</span><strong>FEATURES</strong></div>
    <div class="features-copy">
      <p class="lorem left">Lorem Ipsum is simply dummy text of the printing and typesetting industry. Lorem Ipsum has been the industry's standard dummy text ever since the 1500s, when an unknown</p>
      <h4>Lorem Ipsum is simply dummy</h4>
      <p class="lorem left">Lorem Ipsum is simply dummy text of the printing and typesetting industry. orem Ipsum has been the industry's standard dummy text ever since the 1500s.</p>
    </div>
    <div class="features-aside">
      <h4>Lorem Ipsum is simply dummy text of the printing.</h4>
      <p class="lorem">Lorem Ipsum is simply dummy text of the printing and typesetting industry. Lorem Ipsum has been the industry's standard dummy text ever since the 1500s, when an unknown printer took a galley of type and scrambled.</p>
      <p class="lorem">Lorem Ipsum is simply dummy text of the printing and typesetting industry. Lorem Ipsum has been.</p>
    </div>
    <div class="feature" style="left:183px;top:273px">
      <div class="f-head"><span class="f-icon"><svg width="13" height="13" viewBox="0 0 13 13"><circle cx="6.5" cy="6.5" r="2" fill="#111"/><circle cx="2" cy="2" r="1.3" fill="#111"/><circle cx="11" cy="2" r="1.3" fill="#111"/><circle cx="2" cy="11" r="1.3" fill="#111"/><circle cx="11" cy="11" r="1.3" fill="#111"/><path d="M2 2L11 11M11 2L2 11" stroke="#111" stroke-width=".8"/></svg></span><span class="f-name">FEATUTRE<br>ONE</span></div>
      <p class="lorem">Lorem Ipsum is simply dummy text of the printing and typesetting industry.</p>
    </div>
    <div class="feature" style="left:262px;top:273px">
      <div class="f-head"><span class="f-icon"><svg width="13" height="13" viewBox="0 0 13 13"><rect x="1" y="1" width="9" height="9" fill="none" stroke="#111"/><circle cx="8" cy="8" r="2.5" fill="none" stroke="#111" stroke-width="1.2"/><path d="M10 10l2.5 2.5" stroke="#111" stroke-width="1.3"/></svg></span><span class="f-name">FEATURE<br>TWO</span></div>
      <p class="lorem">Lorem Ipsum is simply dummy text of the etting industry.</p>
    </div>
    <div class="feature" style="left:183px;top:374px">
      <div class="f-head"><span class="f-icon"><svg width="13" height="13" viewBox="0 0 13 13"><path d="M1 9h4l3 1.5 4-2v2l-4 2.5H1z" fill="#111"/><rect x="5" y="1.5" width="3" height="5" fill="#111"/></svg></span><span class="f-name">FEATURE<br>THREE</span></div>
      <p class="lorem">Lorem Ipsum is simply dummy text of the printing and typesetting industry.</p>
    </div>
    <div class="feature" style="left:262px;top:373px">
      <div class="f-head"><span class="f-icon"><svg width="13" height="13" viewBox="0 0 13 13"><circle cx="6.5" cy="6.5" r="4" fill="none" stroke="#111" stroke-width="1.6" stroke-dasharray="2 1.2"/><circle cx="6.5" cy="6.5" r="1.6" fill="#111"/></svg></span><span class="f-name">FEATURE<br>FOUR</span></div>
      <p class="lorem">Lorem Ipsum is simply dummy text of the printing and typesetting industry.</p>
    </div>
  </section>

  <!-- amenities -->
  <section class="page p-amenities">
    <div class="hline" style="left:0;top:30px;width:54px"></div>
    <div class="page-no" style="left:67px;top:24px">3</div>
    <div class="hline" style="left:101px;top:30px;width:144px"></div>
    <div class="brand-mini" style="left:252px;top:19px">Copper Reed Meridian Holdings</div>
    <div class="hline" style="left:313px;top:30px;width:33px"></div>
    <div class="amen-bar"></div>
    <div class="amen-head"><span>OUR COMPANY</span><strong>AMENITIES</strong></div>
    <div class="amenity" style="left:35px;top:128px">
      <div class="a-icon"><svg width="24" height="24" viewBox="0 0 24 24"><path d="M3 16h6l4 2 6-3v3l-6 4H3z" fill="#fff"/><path d="M8 12l4-4 3 3 5-6" stroke="#fff" stroke-width="1.6" fill="none"/></svg></div>
      <h5>Amenities One</h5><div class="a-sub">Lorem Ipsum</div>
      <p class="lorem">Lorem Ipsum is simply dummy text of the printing and typesetting industry. Lorem Ipsum has been the industry'stest wil standard dummy text ever since the 1500s, when an unknown printer took a galley of type and scrambled it to make a type specimen book. It has survived not only five centu.</p>
    </div>
    <div class="amenity" style="left:134px;top:128px">
      <div class="a-icon"><svg width="24" height="24" viewBox="0 0 24 24"><circle cx="12" cy="5" r="3" fill="#fff"/><rect x="9" y="9" width="6" height="5" fill="#fff"/><path d="M3 16h6l4 2 6-3v3l-6 4H3z" fill="#fff"/></svg></div>
      <h5>Amenities Two</h5><div class="a-sub">Lorem Ipsum</div>
      <p class="lorem">Lorem Ipsum is simply dummy text of the printing and typesetting industry. Lorem Ipsum has been the industry'stest wil standard dummy text ever since the 1500s, when an unknown printer took a galley of type and scrambled it to make a type specimen book. It has survived not only five centu.</p>
    </div>
    <div class="amenity" style="left:229px;top:128px">
      <div class="a-icon"><svg width="24" height="24" viewBox="0 0 24 24"><circle cx="14" cy="8" r="4.5" fill="none" stroke="#fff" stroke-width="1.6"/><path d="M12 8l1.5 1.5 3-3" stroke="#fff" stroke-width="1.3" fill="none"/><path d="M3 16h6l4 2 6-3v3l-6 4H3z" fill="#fff"/></svg></div>
      <h5>Amenities Three</h5><div class="a-sub">Lorem Ipsum</div>
      <p class="lorem">Lorem Ipsum is simply dummy text of the printing and typesetting industry. Lorem Ipsum has been the industry'stest wil standard dummy text ever since the 1500s, when an unknown printer took a galley of type and scrambled it to make a type specimen book. It has survived not only five centu.</p>
    </div>
    <svg class="amen-photo" viewBox="0 0 120 103" role="img" aria-label="Aerial photo of the facility buildings and grounds">
      <defs><linearGradient id="aerialTone" x1="0" y1="0" x2="1" y2="1"><stop offset="0" stop-color="#8c8c8c"/><stop offset=".5" stop-color="#b8b8b8"/><stop offset="1" stop-color="#5a5a5a"/></linearGradient></defs>
      <rect width="120" height="103" fill="url(#aerialTone)"/>
    </svg>
    <div class="testi">
      <h6>OUR CLIENT TESTIMONIALS</h6>
      <div class="quote">"</div>
      <p class="lorem">&nbsp;&nbsp;&nbsp;Lorem Ipsum is simply dummy text of he printing and typesetting industry. Lorem Ipsum has been the industry's standard dummy text ever since the 1500s, when an unknown printer took</p>
      <ul><li>Lorem Ipsum is simply dummy</li><li>Lorem Ipsum is simply dummy</li><li>Lorem Ipsum is simply dummy</li></ul>
    </div>
  </section>

  <!-- team -->
  <section class="page p-team">
    <svg class="team-photo" viewBox="0 0 346 234" role="img" aria-label="Photo of a team joining hands around a table">
      <defs><linearGradient id="teamTone" x1="0" y1="0" x2="1" y2="0"><stop offset="0" stop-color="#1f1f1f"/><stop offset=".6" stop-color="#3c3c3c"/><stop offset="1" stop-color="#262626"/></linearGradient></defs>
      <rect width="346" height="234" fill="url(#teamTone)"/>
    </svg>
    <div class="hline" style="left:0;top:30px;width:52px;background:#aaa"></div>
    <div class="brand-mini light" style="left:57px;top:20px">Copper Reed Meridian Holdings</div>
    <div class="hline" style="left:122px;top:30px;width:141px;background:#aaa"></div>
    <div class="page-no" style="left:262px;top:24px;background:transparent;color:#fff;border-color:#fff">4</div>
    <div class="hline" style="left:306px;top:30px;width:40px;background:#aaa"></div>
    <div class="team-head"><span>MEET</span><strong>OUR TEAM</strong></div>
    <svg class="team-shapes" viewBox="0 0 346 488">
      <defs><linearGradient id="portraitTone" x1="0" y1="0" x2="0" y2="1"><stop offset="0" stop-color="#e2e2e2"/><stop offset="1" stop-color="#9d9d9d"/></linearGradient></defs>
      <polygon points="175,176 318,176 248,311" fill="#0a0a0a"/>
      <polygon points="204,244 240,310 204,318 168,310" fill="url(#portraitTone)" role="img" aria-label="Portrait of a team member"/>
      <polygon points="178,313 212,316 178,380 144,347" fill="url(#portraitTone)" role="img" aria-label="Portrait of a team member"/>
      <polygon points="218,313 252,313 218,380 184,380" fill="url(#portraitTone)" role="img" aria-label="Portrait of a team member"/>
      <polygon points="128,382 202,382 165,450" fill="url(#portraitTone)" role="img" aria-label="Portrait of a team member"/>
    </svg>
    <div class="team-brand">Copper Reed Meridian Holdings</div>
    <div class="member right" style="left:26px;top:260px"><h5>NAME HERE</h5><p>Lorem Ipsum is simply dummy text of the printing and typesetting industry.</p></div>
    <div class="member right" style="left:26px;top:328px"><h5>NAME HERE</h5><p>Lorem Ipsum is simply dummy text of the printing and typesetting industry.</p></div>
    <div class="member right" style="left:26px;top:392px"><h5>NAME HERE</h5><p>Lorem Ipsum is simply dummy text of the printing and typesetting industry.</p></div>
    <div class="member" style="left:202px;top:395px"><h5>NAME HERE</h5><p>Lorem Ipsum is simply dummy text of the printing and typesetting industry.</p></div>
  </section>

</main>
</body>
</html>
```